Do i have coronavirus, flue or cold?

Using information from QRV and government agencies we want to make a easy to read infographic helping patients see if they have coronavirus, the flu or a cold. Using a flow diagram or whatever you think will make it easy to read and digest for the average lamen.

Information is in the word document and in the chart.

We are www.tovipharm.co.uk attached is our brand guidelines, we will be putting this infographic on our website and email/sms it to all of our 300,000 patients.

```html
<!DOCTYPE html>
<html lang="en">
<head>
<meta charset="utf-8">
<title>Do I have coronavirus, flu or cold?</title>
<link rel="stylesheet" href="https://fonts.googleapis.com/css2?family=Hind:wght@400;500&family=Nunito:wght@800;900&display=swap">
<style>
  :root {
    --navy: #3235b8;
    --sky: #6b8bee;
    --orange: #f05a22;
    --row: #e2ecf3;
    --divider: #8f94d8;
    --paper: #ffffff;
    --ink: #2c2fa8;
  }
  * { box-sizing: border-box; margin: 0; padding: 0; }
  html, body {
    width: 1200px; height: 2500px; overflow: hidden;
    background: var(--paper);
    font-family: "Hind", sans-serif;
    color: var(--ink);
  }
  .canvas {
    position: relative; width: 1250px; height: 2600px;
    transform: scale(0.96); transform-origin: 0 0;
  }
  .note {
    position: absolute; left: 67px; top: 82px;
    font-size: 30px; color: var(--navy); font-weight: 400;
  }
  .sheet {
    position: absolute; left: 56px; top: 190px; width: 1124px; height: 2340px;
    background: var(--paper);
    box-shadow: 0 2px 12px rgba(0,0,0,.18);
    overflow: hidden;
  }
  .band { position: absolute; }
  .band--edge-light { left: 0; top: 0; width: 51px; height: 270px; background: var(--sky); }
  .band--edge-dark { left: 0; top: 350px; width: 51px; height: 1990px; background: var(--navy); }
  .band--column { left: 51px; top: 520px; width: 503px; height: 1820px; background: var(--navy); }
  .band--corner-light { left: 1075px; top: 0; width: 24px; height: 110px; background: var(--sky); }
  .band--corner-dark { left: 1099px; top: 0; width: 25px; height: 220px; background: var(--navy); }
  .band--foot-light { left: 1017px; top: 2293px; width: 107px; height: 24px; background: var(--sky); }
  .band--foot-dark { left: 906px; top: 2317px; width: 218px; height: 23px; background: var(--navy); }

  .brand {
    position: absolute; left: 94px; top: 50px;
    display: flex; align-items: center; gap: 12px;
  }
  .brand__dot { width: 30px; height: 30px; border-radius: 50%; background: var(--navy); }
  .brand__name { font-family: "Nunito", sans-serif; font-weight: 800; font-size: 40px; color: var(--navy); }

  .headline {
    position: absolute; left: 94px; top: 210px;
    font-family: "Nunito", sans-serif; font-weight: 900; color: var(--navy);
    line-height: 0.98;
  }
  .headline__lead { display: block; color: var(--orange); font-weight: 800; font-size: 72px; margin-bottom: 8px; }
  .headline__main { display: block; font-size: 84px; letter-spacing: -0.5px; }

  .hero {
    position: absolute; left: 590px; top: 30px; width: 460px; height: 520px;
    border-radius: 230px 230px 40px 40px;
    background: linear-gradient(180deg, #eaf1f8 0%, #e6ecf7 45%, #9fb0e4 80%, #4348c4 100%);
  }

  .colhead {
    position: absolute; top: 585px; font-size: 38px; font-weight: 500;
    transform: translateX(-50%); white-space: nowrap;
  }
  .colhead--symptom { left: 340px; color: var(--paper); }
  .colhead--covid { left: 682px; color: var(--navy); }
  .colhead--flu { left: 853px; color: var(--navy); }
  .colhead--cold { left: 1005px; color: var(--navy); }

  .symptom {
    position: absolute; left: 209px; width: 878px; height: 108px;
    background: var(--row);
  }
  .symptom--tall { height: 145px; }
  .symptom__avatar {
    position: absolute; left: -134px; top: 50%; margin-top: -78px;
    width: 156px; height: 156px; border-radius: 50%;
    background: radial-gradient(circle at 50% 45%, #f3f7fb 0 48%, #6b74d6 70%, #3235b8 100%);
    border: 7px solid var(--row);
  }
  .symptom__name {
    position: absolute; left: 47px; top: 50%; transform: translateY(-50%);
    font-family: "Nunito", sans-serif; font-weight: 900; font-size: 50px;
    line-height: 48px; color: var(--navy);
  }
  .symptom__cell {
    position: absolute; top: 0; height: 100%;
    display: flex; flex-direction: column; align-items: center; justify-content: center;
    text-align: center; color: var(--navy);
  }
  .symptom__cell--covid { left: 410px; width: 150px; }
  .symptom__cell--flu { left: 570px; width: 160px; }
  .symptom__cell--cold { left: 730px; width: 150px; }
  .symptom__cell::before {
    content: ""; position: absolute; left: 0; top: 14px; bottom: 14px;
    border-left: 3px solid var(--divider);
  }
  .symptom__cell--covid::before { display: none; }
  .tick { font-family: "Nunito", sans-serif; font-weight: 900; font-size: 46px; line-height: 44px; }
  .cross { font-family: "Nunito", sans-serif; font-weight: 900; font-size: 48px; line-height: 46px; color: var(--orange); }
  .word { font-size: 23px; line-height: 1; }
  .sub { font-size: 23px; line-height: 1; margin-top: 4px; }
  .fine {
    font-size: 18px; line-height: 17px; text-align: left; align-self: flex-start;
    padding: 0 0 0 12px;
  }
  .symptom__cell--covid .fine { padding-left: 0; margin-left: -28px; width: 178px; }
  .symptom__cell .fine-wrap { height: 100%; display: flex; align-items: flex-start; padding-top: 16px; width: 100%; }
</style>
</head>
<body>
<div class="canvas">
  <p class="note">any suggestion for improvement greatly appreciated.</p>

  <section class="sheet">
    <div class="band band--edge-light"></div>
    <div class="band band--edge-dark"></div>
    <div class="band band--column"></div>
    <div class="band band--corner-light"></div>
    <div class="band band--corner-dark"></div>
    <div class="band band--foot-light"></div>
    <div class="band band--foot-dark"></div>

    <div class="brand"><span class="brand__dot"></span><span class="brand__name">Tovipharm</span></div>

    <h1 class="headline">
      <span class="headline__lead">Do i have</span>
      <span class="headline__main">coronavirus,</span>
      <span class="headline__main">flu or cold?</span>
    </h1>

    <div class="hero" role="img" aria-label="Illustration of an unwell woman wrapped in a blanket with a thermometer and a tissue box"></div>

    <span class="colhead colhead--symptom">Symptom</span>
    <span class="colhead colhead--covid">Coronavirus</span>
    <span class="colhead colhead--flu">Flu</span>
    <span class="colhead colhead--cold">Cold</span>

    <div class="symptom" style="top:650px">
      <div class="symptom__avatar" role="img" aria-label="Illustration of a person with a fever and thermometer"></div>
      <div class="symptom__name">Fever</div>
      <div class="symptom__cell symptom__cell--covid"><span class="tick">√</span></div>
      <div class="symptom__cell symptom__cell--flu"><span class="tick">√</span><span class="sub">High</span></div>
      <div class="symptom__cell symptom__cell--cold"><span class="word">Rare</span></div>
    </div>

    <div class="symptom" style="top:815px">
      <div class="symptom__avatar" role="img" aria-label="Illustration of a person coughing"></div>
      <div class="symptom__name">Cough</div>
      <div class="symptom__cell symptom__cell--covid"><span class="tick">√</span><span class="sub">Dry cough</span></div>
      <div class="symptom__cell symptom__cell--flu"><span class="tick">√</span></div>
      <div class="symptom__cell symptom__cell--cold"><span class="word">Moderate</span></div>
    </div>

    <div class="symptom" style="top:980px">
      <div class="symptom__avatar" role="img" aria-label="Illustration of a tired person"></div>
      <div class="symptom__name">Tiredness</div>
      <div class="symptom__cell symptom__cell--covid"><span class="tick">√</span></div>
      <div class="symptom__cell symptom__cell--flu"><span class="tick">√</span></div>
      <div class="symptom__cell symptom__cell--cold"><span class="word">Mild</span></div>
    </div>

    <div class="symptom" style="top:1144px">
      <div class="symptom__avatar" role="img" aria-label="Illustration of a person short of breath"></div>
      <div class="symptom__name">Shortness<br>of breath</div>
      <div class="symptom__cell symptom__cell--covid"><span class="tick">√</span></div>
      <div class="symptom__cell symptom__cell--flu"><span class="tick">√</span></div>
      <div class="symptom__cell symptom__cell--cold"><span class="word">Rare</span></div>
    </div>

    <div class="symptom" style="top:1309px">
      <div class="symptom__avatar" role="img" aria-label="Illustration of a person with aching muscles"></div>
      <div class="symptom__name">Muscle<br>aches</div>
      <div class="symptom__cell symptom__cell--covid"><span class="tick">√</span></div>
      <div class="symptom__cell symptom__cell--flu"><span class="tick">√</span><span class="sub">often</span></div>
      <div class="symptom__cell symptom__cell--cold"><span class="word">Moderate</span></div>
    </div>

    <div class="symptom" style="top:1474px">
      <div class="symptom__avatar" role="img" aria-label="Illustration of a person with a headache"></div>
      <div class="symptom__name">Headache</div>
      <div class="symptom__cell symptom__cell--covid"><span class="word">Sometimes</span></div>
      <div class="symptom__cell symptom__cell--flu"><span class="tick">√</span></div>
      <div class="symptom__cell symptom__cell--cold"><span class="word">Rare</span></div>
    </div>

    <div class="symptom" style="top:1639px">
      <div class="symptom__avatar" role="img" aria-label="Illustration of a person with a sore throat"></div>
      <div class="symptom__name">Sore Throat</div>
      <div class="symptom__cell symptom__cell--covid"><span class="word">Sometimes</span></div>
      <div class="symptom__cell symptom__cell--flu"><span class="word">Sometimes</span></div>
      <div class="symptom__cell symptom__cell--cold"><span class="tick">√</span></div>
    </div>

    <div class="symptom" style="top:1808px">
      <div class="symptom__avatar" role="img" aria-label="Illustration of a person with a runny nose"></div>
      <div class="symptom__name">Stuffy or<br>runny nose</div>
      <div class="symptom__cell symptom__cell--covid"><span class="word">Rare</span></div>
      <div class="symptom__cell symptom__cell--flu"><span class="word">Sometimes</span></div>
      <div class="symptom__cell symptom__cell--cold"><span class="tick">√</span></div>
    </div>

    <div class="symptom" style="top:1968px">
      <div class="symptom__avatar" role="img" aria-label="Illustration of a person sneezing into a tissue"></div>
      <div class="symptom__name">Sneezing</div>
      <div class="symptom__cell symptom__cell--covid"><span class="cross">X</span></div>
      <div class="symptom__cell symptom__cell--flu"><span class="word">Sometimes</span></div>
      <div class="symptom__cell symptom__cell--cold"><span class="tick">√</span></div>
    </div>

    <div class="symptom symptom--tall" style="top:2115px">
      <div class="symptom__avatar" role="img" aria-label="Illustration of a person hugging themselves, feeling unwell"></div>
      <div class="symptom__name">Others</div>
      <div class="symptom__cell symptom__cell--covid"><div class="fine-wrap"><p class="fine">symptoms are usually mild and begin gradually. Some people become infected but don't develop any symptoms and don't feel unwell.</p></div></div>
      <div class="symptom__cell symptom__cell--flu"><div class="fine-wrap"><p class="fine">Some people may have vomiting and diarrhoea</p></div></div>
      <div class="symptom__cell symptom__cell--cold"><div class="fine-wrap"><p class="fine">raised temperature pressure in ears and face loss of taste and smell</p></div></div>
    </div>
  </section>
</div>
</body>
</html>
```